K7 Solutions business card design contest. Use logo and create a professional layout.

See attached sample. Please sharpen all text and images, don't want any pix-elated content. We are looking for a clean look that quickly provides the information need. Please include our information provided on the sample card. Please feel free to offer any design changes. Please only user the colors provided: #2D3539 & #FFA500. Do not prefer any images other than the K7 Logo

Target Market(s)

Construction, Architects, General Contractors, residential

Industry/Entity Type

Business

Contact Information for Business Card

Company logo, Name, email, fax & phone

Font styles to use
Other font styles liked:
• Josefin Slab

Requirements
Must have
• Name
• Phone & Fax #'s
• address
• Logo
• Website url: www.kq7solutions.example
Nice to have
• Font Colors #2D3539 & #FFA400
• We prefer a white background.

```html
<!DOCTYPE html>
<html lang="en">
<head>
<meta charset="utf-8">
<title>K7 Solutions – Business Card</title>
<link href="https://fonts.googleapis.com/css2?family=Montserrat:wght@700&family=Questrial&display=swap" rel="stylesheet">
<style>
  :root {
    --ink: #2D3539;
    --card-white: #ffffff;
    --page: #ffffff;
    --muted: #6e7477;
    --edge: #c9cbcc;
  }
  html, body {
    margin: 0;
    width: 1200px;
    height: 1200px;
    overflow: hidden;
    background: var(--page);
  }
  .sheet {
    position: relative;
    width: 1200px;
    height: 1200px;
    font-family: "Questrial", "Helvetica Neue", Arial, sans-serif;
    color: var(--ink);
  }
  .card {
    position: absolute;
    left: 307px;
    width: 551px;
    height: 314px;
    box-sizing: border-box;
    box-shadow: 8px 10px 14px rgba(0,0,0,0.16);
  }
  .card--front {
    top: 214px;
    background: var(--card-white);
    border: 2px solid var(--edge);
  }
  .card--back {
    top: 639px;
    background: var(--ink);
  }
  .brand {
    position: absolute;
    display: flex;
    align-items: center;
    gap: 9px;
    font-family: "Montserrat", Arial, sans-serif;
    font-weight: 700;
    font-size: 22px;
    letter-spacing: 0.2px;
    white-space: nowrap;
  }
  .brand__dot {
    width: 30px;
    height: 30px;
    box-sizing: border-box;
    border: 4px solid currentColor;
    border-radius: 50%;
  }
  .card--front .brand {
    left: 36px;
    top: 28px;
    color: var(--ink);
  }
  .card--back .brand {
    left: 50%;
    top: 100px;
    transform: translateX(-50%);
    color: var(--muted);
  }
  .holder {
    position: absolute;
    left: 0;
    right: 0;
    top: 108px;
    text-align: center;
  }
  .holder__name {
    font-size: 23px;
    letter-spacing: 0.4px;
    line-height: 1;
  }
  .holder__degree {
    font-family: "Montserrat", Arial, sans-serif;
    font-weight: 700;
  }
  .holder__role {
    margin-top: 8px;
    font-size: 16px;
    letter-spacing: 0.3px;
  }
  .address {
    position: absolute;
    left: 34px;
    top: 237px;
    font-size: 13px;
    line-height: 26px;
    letter-spacing: 0.4px;
  }
  .contacts {
    position: absolute;
    right: 22px;
    top: 216px;
    list-style: none;
    margin: 0;
    padding: 0;
    font-size: 13px;
    letter-spacing: 0.4px;
  }
  .contacts li {
    display: flex;
    align-items: center;
    justify-content: flex-end;
    gap: 16px;
    height: 27px;
  }
  .contacts svg {
    width: 16px;
    height: 16px;
    fill: none;
    stroke: var(--ink);
    stroke-width: 1.6;
  }
  .back-url {
    position: absolute;
    left: 0;
    right: 0;
    top: 266px;
    text-align: center;
    font-size: 16px;
    letter-spacing: 0.6px;
    color: var(--muted);
  }
</style>
</head>
<body>
<main class="sheet">

  <section class="card card--front" aria-label="Business card front">
    <div class="brand"><span class="brand__dot"></span>K7 Solutions</div>

    <div class="holder">
      <div class="holder__name">Marcus D. Ellery, <span class="holder__degree">MBA</span></div>
      <div class="holder__role">Director of Opertion</div>
    </div>

    <address class="address" style="font-style:normal">
      2170 harlow ridge Road, Suite 140-218<br>
      Alder Falls, Georgia, 30099
    </address>

    <ul class="contacts">
      <li>(555)010-2046
        <svg viewBox="0 0 16 16" aria-label="Mobile"><rect x="4.5" y="1.5" width="7" height="13" rx="1.2"/><line x1="7" y1="12" x2="9" y2="12"/></svg>
      </li>
      <li>(555)010-4187
        <svg viewBox="0 0 16 16" aria-label="Fax"><rect x="4.5" y="1.5" width="7" height="4" fill="#2D3539"/><rect x="1.5" y="5.5" width="13" height="6" rx="1" fill="#2D3539"/><rect x="4.5" y="10" width="7" height="4.5" fill="#fff"/></svg>
      </li>
      <li>www.kq7solutions.example
        <svg viewBox="0 0 16 16" aria-label="Website"><circle cx="8" cy="8" r="6.5"/><ellipse cx="8" cy="8" rx="2.8" ry="6.5"/><line x1="1.5" y1="8" x2="14.5" y2="8"/><line x1="2.6" y1="4.6" x2="13.4" y2="4.6"/><line x1="2.6" y1="11.4" x2="13.4" y2="11.4"/></svg>
      </li>
    </ul>
  </section>

  <section class="card card--back" aria-label="Business card back">
    <div class="brand"><span class="brand__dot"></span>K7 Solutions</div>
    <div class="back-url">www.kq7solutions.example</div>
  </section>

</main>
</body>
</html>
```